Training Consultant for Oil and Gas Drillers needs logo for business cards

I teach oil and gas professionals the skills required to keep rigs from blowing up. The company name is "Night Shift Bore Safety", which is pronounced Nite Shiffed. Tour refers to the time on an oil rig when a worker is off for sleep and rest. I teach something called Well Control, which is how to maintain a pressure balance in the well so the hydro carbons don't come to surface unexpectedly( like the Grey Tide Platform).

Target Market(s)

Rig hands and oil companies

Contact Information for Business Card

Night Shift BS ( company name) with a new logo
My name (Derek Holloway )and Title (Well Control Consultant)
Phone number and address

Font styles to use
Serif
Sans Serif

Colors

Designer to choose colors to be used in the design.

Requirements
Must have
• I need a logo for the company. I do not have anything yet

```html
<!DOCTYPE html>
<html lang="en">
<head>
<meta charset="utf-8">
<title>Night Shift BS — Business Cards</title>
<link rel="stylesheet" href="https://fonts.googleapis.com/css2?family=Montserrat:wght@400;500;700&display=swap">
<style>
  :root {
    --backdrop: #a6a6a6;
    --card: #f7f7f5;
    --ink: #2a2a2c;
    --muted: #8d8d90;
    --brand-red: #b10f1d;
    --card-shadow: 0 18px 30px rgba(0,0,0,0.22);
  }
  * { box-sizing: border-box; margin: 0; padding: 0; }
  html, body {
    width: 1200px; height: 800px; overflow: hidden;
    background: var(--backdrop);
    font-family: "Montserrat", sans-serif;
    color: var(--ink);
  }
  .sheet {
    width: 1200px; height: 800px;
    display: flex; align-items: center; justify-content: center; gap: 50px;
  }
  .card {
    position: relative;
    width: 525px; height: 300px;
    background: var(--card);
    box-shadow: var(--card-shadow);
    overflow: hidden;
  }

  /* Front */
  .front-brand {
    position: absolute; left: 0; right: 0; top: 88px;
    display: flex; align-items: center; justify-content: center; gap: 14px;
  }
  .brand-square {
    width: 26px; height: 26px; background: var(--brand-red);
  }
  .brand-name {
    font-weight: 700; font-size: 36px; letter-spacing: 0.5px;
    color: var(--ink); text-transform: uppercase;
  }
  .front-band {
    position: absolute; left: 0; right: 0; bottom: 0; height: 78px;
    background: var(--brand-red);
  }

  /* Back */
  .back-contact {
    position: absolute; left: 40px; top: 52px;
  }
  .person-name {
    font-weight: 700; font-size: 20px; letter-spacing: 0.6px; text-transform: uppercase;
  }
  .person-title {
    margin-top: 8px; font-weight: 500; font-size: 11px; letter-spacing: 0.8px; text-transform: uppercase;
  }
  .contact-lines {
    margin-top: 34px; list-style: none;
    font-weight: 500; font-size: 11px; letter-spacing: 0.5px; line-height: 2; text-transform: uppercase;
  }
  .back-brand {
    position: absolute; right: 34px; top: 112px;
    display: flex; align-items: center; gap: 8px;
  }
  .back-brand .brand-square { width: 14px; height: 14px; }
  .back-brand .brand-name { font-size: 19px; }
  .back-wedge {
    position: absolute; inset: 0; width: 100%; height: 100%;
  }
</style>
</head>
<body>
<main class="sheet">
  <section class="card card-back">
    <svg class="back-wedge" viewBox="0 0 525 300" preserveAspectRatio="none" role="img" aria-label="Red wave-textured accent band">
      <polygon points="250,300 525,175 525,300" fill="var(--brand-red)"/>
    </svg>
    <div class="back-contact">
      <h1 class="person-name">Derek Holloway</h1>
      <p class="person-title">Well Control Consultant</p>
      <ul class="contact-lines">
        <li>+01 555 204.7731</li>
        <li>Midland · Derrick Rd. 14 · USA</li>
      </ul>
    </div>
    <div class="back-brand">
      <span class="brand-square"></span>
      <span class="brand-name">Night Shift BS</span>
    </div>
  </section>

  <section class="card card-front">
    <div class="front-brand">
      <span class="brand-square"></span>
      <span class="brand-name">Night Shift BS</span>
    </div>
    <div class="front-band" role="img" aria-label="Red band with fine wave pattern"></div>
  </section>
</main>
</body>
</html>
```